Business Card Design Project

We require a professional business card designed for our consulting organisation that has the same theme and colours as our logo except for the grey.

Colours on the front should predominately be white however some reference to our logo colours except for the grey.

The back of the card should be have background colour that aligns with our logo colour.

Layout, style and design is up to the designer. So send through your designs

Details are attached in the word document project brief.

Target Market(s)

Target market are large corporate organisations

Industry/Entity Type

Business

Requirements
Must have
• Content on the front must have:

Dean Halvorsen
Managing Director

P: 0417 285 394
E: Dean@brevolinkpartners.com
W: www.brevolinkpartners.com

Content on the back must have the words:
Alliances
Placement
Training
Support

Design Colours
Must align to our logo

```html
<!DOCTYPE html>
<html lang="en">
<head>
<meta charset="utf-8">
<title>Brevolink Partners – Business Card</title>
<link href="https://fonts.googleapis.com/css2?family=Questrial&display=swap" rel="stylesheet">
<style>
  :root {
    --white: #ffffff;
    --brand-blue: #1a6fb9;
    --text-blue: #1d74c2;
    --ink: #222222;
    --arc-outer: #f1f6fb;
    --arc-inner: #dce9f4;
    --arc-low: #edf3f9;
    --arc-low-faint: #f6f9fc;
  }
  * { margin: 0; padding: 0; box-sizing: border-box; }
  html, body {
    width: 1200px;
    height: 686px;
    overflow: hidden;
    background: var(--white);
  }
  .card {
    position: relative;
    width: 1200px;
    height: 686px;
    background: var(--white);
    overflow: hidden;
    font-family: "Questrial", "Century Gothic", sans-serif;
  }
  .card__arcs {
    position: absolute;
    inset: 0;
  }
  .holder {
    position: absolute;
    right: 59px;
    top: 42px;
    text-align: right;
  }
  .holder__name {
    font-size: 48px;
    font-weight: 400;
    color: var(--text-blue);
    line-height: 56px;
    letter-spacing: 0.3px;
  }
  .holder__title {
    font-size: 23px;
    color: var(--ink);
    line-height: 28px;
    margin-top: -2px;
  }
  .brand__mark {
    position: absolute;
    left: 190px;
    top: 98px;
    width: 220px;
    height: 220px;
    border-radius: 50%;
    background: var(--brand-blue);
  }
  .brand__name {
    position: absolute;
    left: 74px;
    top: 428px;
    font-size: 68px;
    line-height: 72px;
    color: var(--brand-blue);
    font-weight: 400;
  }
  .divider {
    position: absolute;
    left: 597px;
    top: 386px;
    width: 3px;
    height: 244px;
    background: var(--brand-blue);
  }
  .contact {
    position: absolute;
    left: 652px;
    top: 455px;
    list-style: none;
    font-size: 23px;
    line-height: 30.5px;
    color: var(--text-blue);
  }
  .contact__row { display: flex; }
  .contact__label { width: 82px; }
  .contact__sep { width: 18px; }
</style>
</head>
<body>
  <main class="card">
    <svg class="card__arcs" width="1200" height="686" viewBox="0 0 1200 686" aria-hidden="true">
      <circle cx="1060" cy="-60" r="465" fill="var(--arc-outer)"/>
      <circle cx="1060" cy="-60" r="410" fill="var(--arc-inner)"/>
      <circle cx="1390" cy="770" r="520" fill="var(--arc-low-faint)"/>
      <circle cx="1380" cy="760" r="500" fill="var(--arc-low)"/>
    </svg>

    <header class="holder">
      <h1 class="holder__name">Dean Halvorsen</h1>
      <p class="holder__title">Managing Director</p>
    </header>

    <div class="brand__mark"></div>
    <p class="brand__name">Brevolink<br>Partners</p>

    <div class="divider"></div>

    <ul class="contact">
      <li class="contact__row"><span class="contact__label">Phone</span><span class="contact__sep">:</span><span>0417 285 394</span></li>
      <li class="contact__row"><span class="contact__label">Email</span><span class="contact__sep">:</span><span>Dean@brevolinkpartners.com</span></li>
      <li class="contact__row"><span class="contact__label">Web</span><span class="contact__sep">:</span><span>www.brevolinkpartners.com</span></li>
    </ul>
  </main>
</body>
</html>
```